Business Card Design Project

Name Martin Holroyd
Company Veldmark Site Restoration Crew
address 22/7 Penbrook street
Wattle Downs
Brisbane Queensland
Australia 4110,
0498357261

Things that we do Mould inspection and Remediation,
Crime and Trauma Scene Cleanup and Decontamination
Drug lab Decontamination and needle cleanups.
Odor control
Air quality Testing and swabs,
latest equipment
Hydroxyl machines, ozone machines ,Sterilising lights ,Comercial Steam machines ,
Thermal imaging, Bacteria testing equipment
Fully trained personel

Reason: One day is not enough time to get designs i dont why the Current deadline is only one day

I do not need purovex in the cards, that was only a sample, The Business name isĀ 

Veldmark Site Restoration Crew.

Target Market(s)

Government agencies ,Police and real-estates, housing companies, Coroners

Industry/Entity Type

Business

Requirements
Must have
• Must tell what we are about
Nice to have
• raised letters or good background

```html
<!DOCTYPE html>
<html lang="en">
<head>
<meta charset="utf-8">
<title>Veldmark Site Restoration Crew – Business Card</title>
<link rel="stylesheet" href="https://fonts.googleapis.com/css2?family=Source+Sans+3:wght@400&family=PT+Sans+Narrow:wght@700&display=swap">
<style>
  :root {
    --page-bg: #e8e5e1;
    --card-black: #000000;
    --emblem-tone: #1a1a1a;
    --text-light: #ffffff;
    --band-yellow: #fff200;
    --text-dark: #000000;
  }
  * { box-sizing: border-box; margin: 0; padding: 0; }
  html, body { width: 1200px; height: 1000px; overflow: hidden; }
  body {
    background: var(--page-bg);
    position: relative;
    font-family: "Source Sans 3", "Myriad Pro", Arial, sans-serif;
  }
  .card {
    position: absolute;
    top: 673px;
    width: 536px;
    height: 300px;
    background: var(--card-black);
    overflow: hidden;
    box-shadow: 0 4px 10px rgba(0,0,0,0.35);
    color: var(--text-light);
    text-align: center;
  }
  .card--front { left: 47px; }
  .card--back { left: 618px; }
  .emblem-area {
    position: absolute;
    border-radius: 50%;
    background: radial-gradient(circle, var(--emblem-tone) 0%, rgba(26,26,26,0.6) 55%, rgba(0,0,0,0) 72%);
  }
  .card--front .emblem-area { left: 60px; top: -40px; width: 520px; height: 420px; }
  .card--back .emblem-area { left: 160px; top: 37px; width: 216px; height: 210px; }
  .company {
    position: absolute;
    left: 0; right: 0;
    font-size: 23px;
    line-height: 30px;
    font-weight: 400;
    white-space: nowrap;
  }
  .card--front .company { top: 34px; }
  .card--back .company { top: 134px; }
  .person-name {
    position: absolute;
    left: 0; right: 0;
    top: 106px;
    font-size: 23px;
    line-height: 28px;
    font-weight: 400;
  }
  .contact-band {
    position: absolute;
    left: 0; right: 0;
    top: 188px;
    height: 76px;
    background: var(--band-yellow);
    color: var(--text-dark);
    font-family: "PT Sans Narrow", "Arial Narrow", sans-serif;
    font-weight: 700;
    white-space: nowrap;
  }
  .phone {
    position: absolute; left: 0; right: 0; top: 10px;
    font-size: 19px; line-height: 24px; letter-spacing: 0.5px;
  }
  .address {
    position: absolute; left: 0; right: 0; top: 43px;
    font-size: 18px; line-height: 24px;
  }
</style>
</head>
<body>
  <section class="card card--front" aria-label="Card front">
    <div class="emblem-area" role="img" aria-label="Faint large hazard emblem decoration"></div>
    <p class="company">Veldmark Site Restoration Crew</p>
    <p class="person-name">Martin Holroyd</p>
    <div class="contact-band">
      <span class="phone">0498357261</span>
      <span class="address">22/7 Penbrook street, Wattle Downs, Kestrel Point Southland, Aurelia 5820,</span>
    </div>
  </section>
  <section class="card card--back" aria-label="Card back">
    <div class="emblem-area" role="img" aria-label="Faint hazard emblem decoration"></div>
    <p class="company">Veldmark Site Restoration Crew</p>
  </section>
</body>
</html>
```